Appointments cards for my business "Bluebell slimming clinic"

I need an appointment card for my business, I will attach the current business card, the logo its self will stay the same, I will attach my most recent personal business card as well. Im looking for a cross in-between both cards not to fancy though.
the back of the card will have the appointment date and time on it... But I don't want my photo on these appointment cards. thank you

Target Market(s)

25-50 year old

Industry/Entity Type

Health Care

Contact Information for Business Card

Bluebell Slimming & Balance clinic
1746 brook st ste#2
sounth ogden ut 84405
phone# (555) 214-7720
fax# (555)214-7721
bluebellslimclinic.com

Font styles to use
Serif
Sans Serif
Script

Colors

Designer to choose colors to be used in the design.

Requirements
Must have
• the logo the address ...info
Nice to have
• I would like to mix my new card with logo and my business card
Should not have
• see above

```html
<!DOCTYPE html>
<html lang="en">
<head>
<meta charset="utf-8">
<title>Bluebell Slimming &amp; Balance clinic – Appointment Card</title>
<link rel="stylesheet" href="https://fonts.googleapis.com/css2?family=Cinzel:wght@400;700&family=Libre+Baskerville:ital,wght@0,400;0,700;1,400&family=Lato:wght@400;700&display=swap">
<style>
  :root {
    --backdrop: #e9e6df;
    --card: #ffffff;
    --rust: #b0603a;
    --maroon: #7a2a1a;
    --bullet: #f0a24a;
    --ink: #1f1f1f;
    --muted: #6a6a6a;
    --ghost: #f1e7e0;
  }
  * { box-sizing: border-box; margin: 0; padding: 0; }
  html, body { width: 1200px; height: 800px; overflow: hidden; }
  body { background: var(--backdrop); position: relative; font-family: "Libre Baskerville", serif; color: var(--ink); }

  .card {
    position: absolute; width: 560px; height: 320px;
    background: var(--card);
    box-shadow: 0 6px 18px rgba(0,0,0,.18);
    overflow: hidden;
  }
  .card--conditions { left: 50px; top: 60px; }
  .card--appointment { left: 590px; top: 420px; }

  /* Brand lockup */
  .brand { position: absolute; display: flex; align-items: center; gap: 8px; }
  .brand__dot { width: 16px; height: 16px; border-radius: 50%; background: var(--rust); flex: none; }
  .brand__name { font-family: "Libre Baskerville", serif; font-size: 12px; line-height: 1.3; color: var(--maroon); width: 150px; }

  /* Conditions side */
  .conditions__band {
    height: 38px; background: var(--rust);
    color: #fbe9dc; font-size: 14px; padding: 11px 24px 0;
  }
  .conditions__backdrop {
    position: absolute; left: 150px; top: 70px; width: 300px; height: 120px;
    border-radius: 50%; background: var(--ghost);
  }
  .conditions__lists { position: absolute; top: 50px; left: 24px; right: 20px; display: flex; gap: 22px; }
  .condition-list { list-style: none; font-size: 11.5px; line-height: 15.5px; }
  .condition-list li { position: relative; padding-left: 16px; }
  .condition-list li::before {
    content: ""; position: absolute; left: 0; top: 5px; width: 6px; height: 6px;
    border-radius: 50%; background: var(--bullet);
  }
  .conditions__call { position: absolute; left: 24px; bottom: 36px; font-size: 19px; }
  .conditions__web { position: absolute; left: 26px; bottom: 18px; font-size: 11px; }
  .card--conditions .brand { right: 16px; bottom: 70px; }

  /* Appointment side */
  .card--appointment .brand { right: 14px; top: 28px; }
  .appointment__heading {
    position: absolute; left: 200px; top: 66px;
    font-style: italic; font-size: 17px; color: var(--maroon);
  }
  .appointment__line { position: absolute; height: 1px; background: var(--maroon); }
  .appointment__label { position: absolute; font-size: 12px; font-weight: 700; color: var(--maroon); }
  .appointment__ghost {
    position: absolute; left: 30px; top: 128px;
    font-size: 62px; color: var(--ghost); white-space: nowrap;
  }
  .appointment__slogan {
    position: absolute; left: 60px; top: 150px;
    font-size: 30px; color: var(--rust); white-space: nowrap;
  }
  .appointment__person { position: absolute; left: 30px; bottom: 40px; }
  .person__name { font-family: "Cinzel", serif; font-weight: 700; font-size: 15px; letter-spacing: 1px; }
  .person__first { color: var(--rust); }
  .person__role { font-family: "Lato", sans-serif; font-size: 14px; color: var(--rust); }
  .appointment__contact {
    position: absolute; right: 28px; top: 222px;
    font-family: "Lato", sans-serif; font-size: 13px; color: var(--muted); line-height: 18px;
  }
  .contact__row { display: flex; gap: 8px; align-items: flex-start; margin-bottom: 6px; }
  .contact__row svg { flex: none; margin-top: 2px; }
</style>
</head>
<body>

<section class="card card--conditions">
  <div class="conditions__band">Conditions we address for women and men</div>
  <div class="conditions__backdrop" aria-hidden="true"></div>
  <div class="conditions__lists">
    <ul class="condition-list">
      <li>PCOS</li>
      <li>Hysterectomy</li>
      <li>Type-II Diabetes</li>
      <li>Insulin Resistance</li>
      <li>Hypothyroid</li>
      <li>Underactive Thyroid</li>
      <li>Fibromyalgia</li>
      <li>Chronic Fatigue</li>
      <li>Chronic Headaches &amp; Migraines</li>
      <li>Hypertension</li>
      <li>Elevated Fasting Glucose</li>
    </ul>
    <ul class="condition-list">
      <li>Pre-Diabetes</li>
      <li>Abdominal Obesity</li>
      <li>High Triglycerides</li>
      <li>High Blood Pressure</li>
      <li>High Cholesterol</li>
      <li>Gestational Diabetes</li>
      <li>Epstein Bar</li>
      <li>Infertility</li>
      <li>Infertility Drugs</li>
      <li>Anti-Depression Medications</li>
    </ul>
  </div>
  <div class="brand">
    <span class="brand__dot"></span>
    <span class="brand__name">Bluebell Slimming &amp; Balance clinic</span>
  </div>
  <p class="conditions__call">Call Today!: (555)214-7720</p>
  <p class="conditions__web">www.bluebellslimclinic.com</p>
</section>

<section class="card card--appointment">
  <div class="brand">
    <span class="brand__dot"></span>
    <span class="brand__name">Bluebell Slimming &amp; Balance clinic</span>
  </div>
  <p class="appointment__heading">Appointment On . . .</p>
  <span class="appointment__line" style="left:360px; top:86px; width:170px;"></span>
  <span class="appointment__label" style="left:240px; top:98px;">Time:</span>
  <span class="appointment__line" style="left:285px; top:110px; width:245px;"></span>
  <span class="appointment__label" style="left:30px; top:112px;">Date:</span>
  <span class="appointment__line" style="left:72px; top:124px; width:160px;"></span>
  <div class="appointment__ghost" aria-hidden="true">Let’s Make it</div>
  <p class="appointment__slogan">Let’s Make it Happen</p>
  <div class="appointment__person">
    <p class="person__name"><span class="person__first">Marla</span> Jennings</p>
    <p class="person__role">Director</p>
  </div>
  <div class="appointment__contact">
    <div class="contact__row">
      <svg width="10" height="14" viewBox="0 0 10 14"><path d="M5 0a5 5 0 0 0-5 5c0 4 5 9 5 9s5-5 5-9a5 5 0 0 0-5-5zm0 7a2 2 0 1 1 0-4 2 2 0 0 1 0 4z" fill="#b0603a"/></svg>
      <span>1746 Brook St ste#2<br>Fernridge Valley 84999</span>
    </div>
    <div class="contact__row">
      <svg width="14" height="12" viewBox="0 0 14 12"><path d="M1 4c0-2 3-3 6-3s6 1 6 3v1h-3V3.5H4V5H1zM3 6h8l2 5H1z" fill="#b0603a"/></svg>
      <span>1(555) 214-7720</span>
    </div>
  </div>
</section>

</body>
</html>
```